RW Frameworks Inc Business cards

We need business cards using our existing logo but slightly modified. Right now the logo says RW Framework Masonry. We want to keep the RW part of the design, but replace the Framework Masonry portion with "FRAMEWORKS". Please see the attached file.
Ideally this would be a blank template so we can add Different Names, titles, and phone numbers later.
On the one side we want only the logo and on the other side the detail. I'm attaching an example for you to see.
Please reach out with any other questions. Our address and other details will be given out once we find a design we like.

Target Market(s)

Construction Industry

```html
<!DOCTYPE html>
<html lang="en">
<head>
<meta charset="utf-8">
<title>RW Frameworks Inc — Business Cards</title>
<link href="https://fonts.googleapis.com/css2?family=Russo+One&family=Roboto:wght@400;700&display=swap" rel="stylesheet">
<style>
  :root {
    --backdrop: #a9a9a9;
    --brand-blue: #1a74bd;
    --brand-blue-dark: #1766a8;
    --brand-blue-light: #1f82d1;
    --card-white: #ffffff;
    --text-grey: #555a60;
    --rule-grey: #9a9a9a;
  }
  * { margin: 0; padding: 0; box-sizing: border-box; }
  html, body {
    width: 1200px; height: 1200px; overflow: hidden;
    background: var(--backdrop);
  }
  .stage { position: relative; width: 1200px; height: 1200px; }
  .card {
    position: absolute; top: 303px; width: 369px; height: 594px;
    box-shadow: 3px 4px 6px rgba(0,0,0,0.45);
    overflow: hidden;
  }
  .card-front { left: 201px; background: var(--brand-blue); }
  .card-back { left: 599px; background: var(--card-white); }
  .front-bands { position: absolute; inset: 0; }
  .wordmark {
    position: absolute; left: 0; right: 0; text-align: center;
    font-family: "Russo One", sans-serif; line-height: 1;
  }
  .wordmark-initials { display: block; font-size: 104px; letter-spacing: 2px; }
  .wordmark-name { display: block; font-size: 30px; letter-spacing: 1px; margin-top: 6px; }
  .card-front .wordmark { top: 226px; color: var(--card-white); }
  .card-back .wordmark { top: 112px; color: var(--brand-blue); }
  .front-url {
    position: absolute; left: 0; right: 0; top: 530px; text-align: center;
    font-family: "Roboto", sans-serif; font-weight: 700; font-size: 18px;
    color: var(--card-white);
  }
  .contact-block {
    position: absolute; left: 0; right: 0; top: 394px; text-align: center;
    font-family: "Roboto", sans-serif; color: var(--text-grey);
  }
  .person-name {
    font-family: "Russo One", sans-serif; font-size: 23px;
    color: var(--brand-blue); letter-spacing: 0.5px; line-height: 1.1;
  }
  .person-title { font-size: 17px; line-height: 1.2; }
  .icon-row {
    display: flex; align-items: center; justify-content: center;
    gap: 4px; margin: 12px 0 8px;
  }
  .icon-row .rule { width: 52px; height: 1px; background: var(--rule-grey); margin: 0 4px; }
  .icon-tile {
    width: 25px; height: 25px; border-radius: 3px; background: var(--brand-blue);
    display: flex; align-items: center; justify-content: center;
  }
  .contact-line { font-size: 17px; line-height: 22px; letter-spacing: 0.3px; }
</style>
</head>
<body>
<main class="stage">
  <section class="card card-front" aria-label="Card front">
    <svg class="front-bands" width="369" height="594" viewBox="0 0 369 594" aria-hidden="true">
      <polygon points="327,0 369,0 369,170 0,470 0,265" fill="var(--brand-blue-light)" opacity="0.55"/>
      <polygon points="369,395 369,594 340,594 110,398 190,330" fill="var(--brand-blue-dark)"/>
    </svg>
    <div class="wordmark">
      <span class="wordmark-initials">RW</span>
      <span class="wordmark-name">FRAMEWORKS</span>
    </div>
    <p class="front-url">WWW.RWFRAMEWORKS.COM</p>
  </section>

  <section class="card card-back" aria-label="Card back">
    <div class="wordmark">
      <span class="wordmark-initials">RW</span>
      <span class="wordmark-name">FRAMEWORKS</span>
    </div>
    <div class="contact-block">
      <p class="person-name">DANIEL HART</p>
      <p class="person-title">Managing Director</p>
      <div class="icon-row">
        <span class="rule"></span>
        <span class="icon-tile" aria-label="Phone">
          <svg width="15" height="15" viewBox="0 0 16 16"><path d="M2 6c0-2 3-3 6-3s6 1 6 3l-2 1-1-2H5L4 7zM4 8h8l1 5H3z" fill="#fff"/></svg>
        </span>
        <span class="icon-tile" aria-label="Email">
          <svg width="15" height="12" viewBox="0 0 16 12"><rect x="1" y="1" width="14" height="10" fill="none" stroke="#fff" stroke-width="1.3"/><path d="M1 1l7 6 7-6M1 11l5-5M15 11l-5-5" fill="none" stroke="#fff" stroke-width="1.1"/></svg>
        </span>
        <span class="icon-tile" aria-label="Website">
          <svg width="15" height="15" viewBox="0 0 16 16"><circle cx="8" cy="8" r="6.5" fill="#fff"/><path d="M5 4c2 0 2 2 1 3s1 2 0 3M10 9c1 0 2 1 1 3" fill="none" stroke="var(--brand-blue)" stroke-width="1.4"/></svg>
        </span>
        <span class="rule"></span>
      </div>
      <p class="contact-line">055-246 810 357</p>
      <p class="contact-line">hello@rwframe.com</p>
      <p class="contact-line">www.rwframeworks.com</p>
    </div>
  </section>
</main>
</body>
</html>
```